Dating Coach needs a Book Cover Design

My new book called "When to Turn the Tide: Meeting Romance Among the Endless Crowd of Digital Courtship" needs a cover! I tried to make one on my own, but it's just not my skill set :) Please see attached for my best attempt. I'd like to see the title smaller and the tagline bigger - so that the tagline is easier to read. But I'm not sure how to do this and still have the Title look great. I'm also considering if the "TURN THE TIDE" part should not be in all caps. Looking forward to your ideas! I'm also afraid that the drawing is a bit too cartoonish and doesn't match my brand. I'm looking for something elegant and also very approachable and down to earth. My website is www.petrawendtcoaching.example so you can use as reference! Please see my attached brand style guide for colors. This will be an e-book that I give away for free to anyone who signs up for my newsletter. Some mock-ups would also be great to use in advertising.

```html
<!DOCTYPE html>
<html lang="en">
<head>
<meta charset="utf-8">
<title>The Art of Connection — Book Cover</title>
<link rel="stylesheet" href="https://fonts.googleapis.com/css2?family=Bebas+Neue&family=Oswald:wght@500;600&display=swap">
<style>
  :root {
    --backdrop: #546f79;
    --cover-sky: #b3dbe2;
    --wave-light: #d9eef1;
    --wave-mid: #9ccbd6;
    --boat-orange: #d9672e;
    --title-red: #e1301f;
    --ink-navy: #1f3a4d;
    --band-teal: #3c7383;
    --band-text: #ffffff;
  }
  * { box-sizing: border-box; margin: 0; padding: 0; }
  html, body {
    width: 1194px;
    height: 1200px;
    overflow: hidden;
    background: var(--backdrop);
  }
  .canvas {
    position: relative;
    width: 1194px;
    height: 1200px;
    display: flex;
    align-items: center;
    justify-content: center;
  }
  .book-cover {
    position: relative;
    width: 720px;
    height: 1080px;
    background: var(--cover-sky);
    overflow: hidden;
    box-shadow: 0 20px 40px rgba(0, 0, 0, 0.25);
  }
  .cover-illustration {
    position: absolute;
    left: 0;
    top: 470px;
    width: 720px;
    height: 610px;
    background:
      radial-gradient(ellipse at 50% 62%, rgba(217, 103, 46, 0.55) 0 16%, transparent 30%),
      radial-gradient(ellipse at 50% 95%, var(--wave-light) 0 35%, transparent 60%),
      linear-gradient(180deg, var(--cover-sky) 0%, var(--wave-mid) 55%, var(--wave-light) 100%);
  }
  .cover-header {
    position: absolute;
    left: 0;
    right: 0;
    top: 70px;
    text-align: center;
  }
  .series-label {
    font-family: "Oswald", sans-serif;
    font-weight: 600;
    font-size: 30px;
    letter-spacing: 1px;
    color: var(--ink-navy);
    text-transform: uppercase;
  }
  .book-title {
    font-family: "Bebas Neue", sans-serif;
    font-weight: 400;
    color: var(--title-red);
    text-transform: uppercase;
    line-height: 0.86;
    margin-top: 10px;
  }
  .book-title .line-one { display: block; font-size: 178px; }
  .book-title .line-two { display: block; font-size: 172px; }
  .book-subtitle {
    margin-top: 22px;
    font-family: "Oswald", sans-serif;
    font-weight: 500;
    font-size: 31px;
    line-height: 1.15;
    color: var(--ink-navy);
    text-transform: uppercase;
  }
  .author-band {
    position: absolute;
    left: 0;
    right: 0;
    top: 930px;
    height: 70px;
    background: var(--band-teal);
    display: flex;
    align-items: center;
    justify-content: center;
  }
  .author-name {
    font-family: "Oswald", sans-serif;
    font-weight: 500;
    font-size: 28px;
    letter-spacing: 9px;
    color: var(--band-text);
    text-transform: uppercase;
  }
</style>
</head>
<body>
  <main class="canvas">
    <section class="book-cover">
      <div class="cover-illustration" role="img" aria-label="Illustration of a smiling woman riding an orange wooden boat through swirling waves full of flying envelopes and clocks"></div>
      <header class="cover-header">
        <p class="series-label">Modern Coaching</p>
        <h1 class="book-title">
          <span class="line-one">The Art of</span>
          <span class="line-two">Connection</span>
        </h1>
        <p class="book-subtitle">A Guide to Navigating Online Dating<br>and Finding True Partnership</p>
      </header>
      <div class="author-band">
        <p class="author-name">By Petra J. Wendt</p>
      </div>
    </section>
  </main>
</body>
</html>
```